Melbourne Locksmith Needs a Web Site

We need a web site for our new Locksmith business in Melbourne Australia. Our business is called " Calloway Lane Locksmiths" . (Calloway lane is a well known in the city and has the famous railway station , it is a main icon of melbourne . Maybe we could incorperate the station maybe in the front page or heading background. our services include Automotive Locksmithing ( Cuting keys to cars, opening cars etc / Master Keys Systems/ Commercial work / Domestic . Also we have no logo yet. but we can get that in the future if needed.

Target Market(s)

(Automotive ) Lost keys to cars, Trucks, Jammed Ignitions, Opening Vehicles. mobile locksmith in a van, Locked out of your house ?

Industry/Entity Type

Business

Number of Pages Required

4 page

Font styles to use
Sans Serif

Colors

Designer to choose colors to be used in the design.

Requirements
Must have
• Phone number easy to read on web site.
Nice to have
• map of where we are, show case pictures of common lock problems for automotive eg ( damaged keys/ Broken).

```html
<!DOCTYPE html>
<html lang="en">
<head>
<meta charset="utf-8">
<title>Calloway Lane Locksmith</title>
<link href="https://fonts.googleapis.com/css2?family=Lato:ital,wght@0,400;0,700;1,400&family=Roboto:wght@300;400;500&display=swap" rel="stylesheet">
<style>
:root{
  --orange:#e8771f;
  --blue:#1b56a3;
  --blue-light:#3d73b9;
  --navy:#1d2331;
  --ink:#222;
  --frame:#e6e6e6;
  --white:#fff;
}
*{box-sizing:border-box;margin:0;padding:0}
html,body{width:1200px;height:3364px;overflow:hidden;background:var(--white)}
body{font-family:"Lato",sans-serif;color:var(--ink)}
.page{position:relative;width:1200px;height:3364px;overflow:hidden}
.abs{position:absolute}
.heading{font-family:"Roboto",sans-serif;font-weight:400;text-transform:uppercase;letter-spacing:1px}
.btn{position:absolute;background:var(--orange);color:var(--white);font:700 13px "Lato",sans-serif;text-transform:uppercase;display:flex;align-items:center;justify-content:center;border-radius:2px}
.photo{position:absolute}

/* header */
.site-header{position:absolute;left:0;top:0;width:1200px;height:135px;background:var(--white)}
.brand{position:absolute;left:0;top:0;width:470px;height:135px;background:var(--blue);clip-path:polygon(0 0,100% 0,86% 100%,0 100%)}
.brand-name{position:absolute;left:76px;top:34px;color:var(--white);font:500 27px/1.15 "Roboto",sans-serif;letter-spacing:3px;text-transform:uppercase}
.contact-bar{position:absolute;right:78px;top:22px;display:flex;gap:34px;font:400 18px "Roboto",sans-serif;color:var(--ink)}
.contact-bar span{display:flex;align-items:center;gap:14px}
.main-nav{position:absolute;right:78px;top:78px;display:flex;gap:58px;font:500 16px "Roboto",sans-serif;text-transform:uppercase}
.main-nav a{color:var(--ink);text-decoration:none;padding-bottom:6px}
.main-nav a.active{color:var(--orange);border-bottom:2px solid var(--orange)}

/* hero */
.hero{position:absolute;left:0;top:135px;width:1200px;height:533px;
  background:
    radial-gradient(ellipse 260px 200px at 900px 170px,rgba(214,160,128,.85),rgba(214,160,128,0) 70%),
    radial-gradient(ellipse 220px 130px at 520px 300px,rgba(205,150,118,.75),rgba(205,150,118,0) 70%),
    radial-gradient(ellipse 380px 330px at 960px 470px,rgba(18,18,18,.95),rgba(18,18,18,0) 75%),
    linear-gradient(90deg,#eef1f3 0%,#dfe4e7 18%,#b9c2c8 30%,#8e969b 42%,#6a6f72 55%,#3a3a3a 75%,#1c1c1c 100%)}
.hero-caption{position:absolute;left:0;bottom:0;width:1200px;height:80px;background:rgba(0,0,0,.55);color:var(--white);font:400 24px/1.15 "Roboto",sans-serif;letter-spacing:1.5px;text-align:center;padding-top:13px}
.hero-arrow{position:absolute;top:462px}

/* about */
.section-title{position:absolute;left:0;width:1200px;text-align:center;font-size:31px}
.title-rule{position:absolute;left:480px;width:240px;height:2px;background:#cfcfcf}
.orange{color:var(--orange)}
.blue{color:var(--blue)}
.lead{position:absolute;left:82px;width:1036px;text-align:center;font:700 12.5px/1.45 "Lato",sans-serif}
.body-text{position:absolute;left:82px;width:1036px;text-align:center;font:400 12.5px/1.45 "Lato",sans-serif}

/* services */
.services{position:absolute;left:0;top:1034px;width:1200px;height:451px;color:var(--white);
  background:
    radial-gradient(ellipse 320px 220px at 880px 120px,rgba(90,90,90,.8),rgba(90,90,90,0) 70%),
    radial-gradient(ellipse 260px 160px at 300px 90px,rgba(60,60,60,.7),rgba(60,60,60,0) 70%),
    linear-gradient(120deg,#050505 0%,#262626 40%,#3a3a3a 60%,#0d0d0d 100%)}
.service-card{position:absolute;top:200px;width:233px;height:201px}
.service-card .photo{left:0;top:0;width:233px;height:175px}
.service-label{position:absolute;left:10px;top:157px;width:213px;height:40px;background:var(--blue);color:var(--white);font:400 14.5px "Roboto",sans-serif;text-transform:uppercase;display:flex;align-items:center;justify-content:center}
.service-label.current{background:var(--orange)}

/* feature */
.feature-title{position:absolute;left:81px;top:1536px;color:var(--blue);font:500 16.5px "Roboto",sans-serif}
.feature-text{position:absolute;left:81px;top:1574px;width:680px;font:400 12.5px/1.75 "Lato",sans-serif}
.ticks{position:absolute;left:81px;top:1642px;width:680px;display:grid;grid-template-columns:1fr 1fr;row-gap:16px;list-style:none;font:400 12.5px "Lato",sans-serif}
.ticks li{padding-left:16px;position:relative;border-bottom:1px solid #eee;padding-bottom:10px;white-space:nowrap}
.ticks li::before{content:"";position:absolute;left:2px;top:6px;width:5px;height:5px;border-radius:50%;background:var(--blue)}
.feature-frame{position:absolute;left:794px;top:1530px;width:325px;height:242px;border:1px solid #ddd;padding:8px;background:var(--white);box-shadow:0 1px 4px rgba(0,0,0,.12)}

/* inquiry / testimonial */
.inquiry{position:absolute;left:0;top:1839px;width:601px;height:411px;
  background:radial-gradient(ellipse 300px 220px at 480px 120px,rgba(255,255,255,.06),rgba(255,255,255,0) 70%),var(--blue)}
.testimonial{position:absolute;left:601px;top:1839px;width:599px;height:411px;
  background:radial-gradient(ellipse 300px 220px at 120px 300px,rgba(255,255,255,.07),rgba(255,255,255,0) 70%),var(--orange)}
.panel-title{position:absolute;left:0;top:56px;width:100%;text-align:center;color:var(--white);font:400 29px "Roboto",sans-serif;text-transform:uppercase;letter-spacing:1px}
.field{position:absolute;background:var(--blue-light);border:1px solid #6b94c9;color:#dbe6f4;font:400 11.5px "Lato",sans-serif;padding:10px 12px}
.quote{position:absolute;left:43px;top:218px;width:513px;text-align:center;color:var(--white);font:400 11.5px/1.9 "Lato",sans-serif}
.client-name{position:absolute;left:0;top:326px;width:100%;text-align:center;color:var(--white);font:400 14px "Roboto",sans-serif;text-transform:uppercase}
.client-role{position:absolute;left:0;top:350px;width:100%;text-align:center;color:#fde3cc;font:italic 400 12px "Lato",sans-serif}

/* gallery */
.gallery-item{position:absolute;background:var(--frame);padding:12px;box-shadow:0 1px 3px rgba(0,0,0,.1)}
.gallery-item .photo{position:static;width:100%;height:100%}

/* footer */
.site-footer{position:absolute;left:0;top:3040px;width:1200px;height:269px;background:var(--navy);color:var(--white)}
.footer-head{position:absolute;top:48px;font:400 15px "Roboto",sans-serif;text-transform:uppercase;padding-bottom:8px;border-bottom:1px solid #4a5263;width:120px}
.quick-links{position:absolute;left:81px;top:90px;list-style:none;font:400 13px/29px "Lato",sans-serif}
.contact-list{position:absolute;left:253px;top:88px;list-style:none;font:400 12px/1.4 "Lato",sans-serif}
.contact-list li{display:flex;gap:10px;margin-bottom:14px}
.contact-list strong{font-weight:700}
.footer-brand{position:absolute;left:825px;top:3024px;width:296px;height:285px;background:var(--orange);color:var(--white);text-align:center}
.footer-brand-name{position:absolute;left:0;top:110px;width:100%;font:400 25px/1.25 "Roboto",sans-serif;letter-spacing:4px;text-transform:uppercase}
.follow{position:absolute;left:0;top:200px;width:100%;font:400 12px "Lato",sans-serif}
.socials{position:absolute;left:0;top:236px;width:100%;display:flex;justify-content:center;gap:9px}
.socials span{width:27px;height:27px;background:var(--navy)}
.copyright{position:absolute;left:0;top:3309px;width:1200px;height:55px;background:var(--orange);color:var(--white);font:400 12px "Lato",sans-serif;padding:20px 0 0 79px}
</style>
</head>
<body>
<div class="page">

  <header class="site-header">
    <div class="brand"><div class="brand-name">Calloway Lane<br>Locksmith</div></div>
    <div class="contact-bar">
      <span>
        <svg width="32" height="32" viewBox="0 0 32 32"><circle cx="16" cy="16" r="14" fill="none" stroke="#e8771f" stroke-width="2.5"/><path d="M11 9l3 3-2 2c1 2 3 4 5 5l2-2 3 3-2 3c-5 0-11-6-11-11z" fill="#e8771f"/></svg>
        123-456-7890
      </span>
      <span>
        <svg width="32" height="32" viewBox="0 0 32 32"><circle cx="16" cy="16" r="14" fill="none" stroke="#e8771f" stroke-width="2.5"/><rect x="9" y="11" width="14" height="10" fill="#e8771f"/><path d="M9 11l7 6 7-6" fill="none" stroke="#fff" stroke-width="1.5"/></svg>
        info@callowaylanelocksmith.au
      </span>
    </div>
    <nav class="main-nav">
      <a class="active" href="#">Home</a><a href="#">About Us</a><a href="#">Services</a><a href="#">Gallery</a><a href="#">Contact Us</a>
    </nav>
  </header>

  <section class="hero" role="img" aria-label="Locksmith in a black shirt fitting a cylinder lock into a white door">
    <svg class="hero-arrow" style="left:44px" width="20" height="48" viewBox="0 0 20 48"><path d="M18 2L3 24l15 22" fill="none" stroke="#fff" stroke-width="2"/></svg>
    <svg class="hero-arrow" style="right:44px" width="20" height="48" viewBox="0 0 20 48"><path d="M2 2l15 22L2 46" fill="none" stroke="#fff" stroke-width="2"/></svg>
    <div class="hero-caption">At Calloway Lane Locksmith, We Know What It Takes To Keep Your<br>Home &amp; Business Safe &amp; Secure</div>
  </section>

  <section>
    <h2 class="section-title heading" style="top:708px"><span class="orange">About Calloway Lane</span> <span class="blue">Locksmith</span></h2>
    <div class="title-rule" style="top:764px"></div>
    <p class="lead" style="top:790px">Lorem ipsum dolor sit amet, consectetuer adipiscing elit, sed diam nonummy nibh euismod tincidunt ut laoreet dolore magna aliquam erat volutpat. Ut wisi enim ad minim veniam, quis nostrud exerci tation ullamcorper suscipit lobortis nisl ut aliquip ex ea commodo</p>
    <p class="body-text" style="top:836px">Lorem ipsum dolor sit amet, consectetuer adipiscing elit, sed diam nonummy nibh euismod tincidunt ut laoreet dolore magna aliquam erat volutpat. Ut wisi enim ad minim veniam, quis nostrud exerci tation ullamcorper suscipit lobortis nisl ut aliquip ex ea commodo consequat. Duis autem vel eum iriure dolor in hendrerit in vulputate velit esse molestie consequat, vel illum dolore eu feugiat nulla facilisis at vero eros et accumsan et iusto odio dignissim qui blandit praesent luptatum zzril delenit augue duis dolore te feugait nulla facilisi ex ea commodo consequat. Duis autem vel eum iriure dolor in hendrerit</p>
    <div class="btn" style="left:537px;top:942px;width:126px;height:36px">Read More</div>
  </section>

  <section class="services" role="img" aria-label="Dark close-up of a car door lock">
    <h2 class="section-title heading" style="top:40px;color:#fff">Our Services</h2>
    <div class="title-rule" style="top:96px;left:515px;width:170px;background:#888"></div>
    <p class="lead" style="top:118px;color:#fff">Lorem ipsum dolor sit amet, consectetuer adipiscing elit, sed diam nonummy nibh euismod tincidunt ut laoreet dolore magna aliquam erat volutpat. Ut wisi enim ad minim veniam, quis nostrud exerci tation ullamcorper suscipit lobortis nisl ut aliquip ex ea commodo</p>
    <div class="service-card" style="left:79px"><div class="photo" role="img" aria-label="Key cutting machine" style="background:radial-gradient(ellipse 90px 60px at 150px 40px,#e0b488,rgba(224,180,136,0) 70%),linear-gradient(160deg,#6e7a86 0%,#c08a55 45%,#d5a26a 70%,#7a5636 100%)"></div><div class="service-label current">Cutting Keys to Cars</div></div>
    <div class="service-card" style="left:348px"><div class="photo" role="img" aria-label="Hand opening a car door" style="background:radial-gradient(ellipse 90px 70px at 150px 110px,#d3a083,rgba(211,160,131,0) 70%),linear-gradient(135deg,#cfd4d8 0%,#7d858c 40%,#2f3338 100%)"></div><div class="service-label">Opening Cars</div></div>
    <div class="service-card" style="left:617px"><div class="photo" role="img" aria-label="Hands working on a door lock" style="background:radial-gradient(ellipse 110px 70px at 100px 80px,#d6a47f,rgba(214,164,127,0) 70%),linear-gradient(90deg,#8b6a4e 0%,#c8ab8b 60%,#9b8f84 100%)"></div><div class="service-label">Master Keys Systems</div></div>
    <div class="service-card" style="left:886px"><div class="photo" role="img" aria-label="Hand holding keys at a metal lock" style="background:radial-gradient(ellipse 80px 70px at 130px 90px,#8a8a8a,rgba(138,138,138,0) 70%),linear-gradient(135deg,#f2f2f2 0%,#cfcfcf 50%,#9a9a9a 100%)"></div><div class="service-label">Commercial Work</div></div>
  </section>

  <section>
    <h3 class="feature-title">consectetur adipiscing elit, sed do eiusmod Lorem ipsum dolor sit amet</h3>
    <p class="feature-text">Lorem ipsum dolor sit amet, consectetur adipiscing elit, sed do eiusmod tempor incididunt ut labore et dolore magna aliqua. Ut enim ad minim veniam, quis nostrud exercitation ullamco laboris nisi ut aliquip</p>
    <ul class="ticks">
      <li>Lorem ipsum dolor sit amet, consectetur adipiscing elit,</li>
      <li>Lorem ipsum dolor sit amet, consectetur</li>
      <li>Lorem ipsum dolor sit amet, consectetur adipiscing elit,</li>
      <li>Lorem ipsum dolor sit amet</li>
    </ul>
    <div class="btn" style="left:79px;top:1738px;width:152px;height:36px">Call Us Today</div>
    <div class="feature-frame"><div class="photo" role="img" aria-label="Locksmith in a blue shirt working inside a red car" style="position:static;width:100%;height:100%;background:radial-gradient(ellipse 110px 80px at 190px 150px,#2c4a86,rgba(44,74,134,0) 75%),radial-gradient(ellipse 90px 60px at 260px 40px,#c9a28a,rgba(201,162,138,0) 70%),linear-gradient(135deg,#cf3a30 0%,#a82621 40%,#5a1816 70%,#1f2a45 100%)"></div></div>
  </section>

  <section class="inquiry">
    <h2 class="panel-title">Quick Inquiry</h2>
    <div class="field" style="left:79px;top:103px;width:219px;height:39px">Name</div>
    <div class="field" style="left:316px;top:103px;width:222px;height:39px">Phone</div>
    <div class="field" style="left:79px;top:155px;width:459px;height:38px">Email</div>
    <div class="field" style="left:79px;top:207px;width:459px;height:87px">Message</div>
    <div class="btn" style="left:265px;top:325px;width:89px;height:36px">Submit</div>
  </section>

  <section class="testimonial">
    <h2 class="panel-title">What Our Clients Say</h2>
    <svg class="abs" style="left:206px;top:142px" width="14" height="22" viewBox="0 0 14 22"><path d="M12 2L3 11l9 9" fill="none" stroke="#fff" stroke-width="2.5"/></svg>
    <svg class="abs" style="left:348px;top:142px" width="14" height="22" viewBox="0 0 14 22"><path d="M2 2l9 9-9 9" fill="none" stroke="#fff" stroke-width="2.5"/></svg>
    <div class="abs" role="img" aria-label="Client portrait" style="left:242px;top:106px;width:92px;height:92px;border-radius:50%;background:radial-gradient(circle at 50% 45%,#ecd6c6 0%,#c99d84 60%,#5a3b30 100%);border:4px solid #fff;box-shadow:0 0 0 3px var(--blue)"></div>
    <p class="quote">Donec pulvinar libero eget enim facilisis,ulla accumsan arcu lobortis. Pe impe efficitur ligula. Aliquam non augue vitae mauris pellentesque vulputate, bibendum mauris at ante Convallis sagittis. Vivamus sodales velit odio, quis feugiat lacu Fusce amet sapi dignissim feugiat ligulin erat eget ex sos sodales velit odio, quis feugiat lacinia porta at ud.</p>
    <div class="client-name">Marcus Hollis</div>
    <div class="client-role">(quis feugiat)</div>
  </section>

  <section>
    <h2 class="section-title heading" style="top:2294px"><span class="orange">Lock Problem Solved</span> <span class="blue">Gallery</span></h2>
    <div class="title-rule" style="top:2350px"></div>
    <div class="gallery-item" style="left:79px;top:2398px;width:506px;height:276px"><div class="photo" role="img" aria-label="Locksmith drilling a door lock" style="background:radial-gradient(ellipse 120px 80px at 330px 110px,#c99a7c,rgba(201,154,124,0) 70%),radial-gradient(ellipse 140px 70px at 190px 160px,#3a6a8c,rgba(58,106,140,0) 70%),linear-gradient(90deg,#9aa7b2 0%,#6f7c86 40%,#3a3430 100%)"></div></div>
    <div class="gallery-item" style="left:601px;top:2398px;width:247px;height:343px"><div class="photo" role="img" aria-label="Two locksmiths at a doorway with a toolbox" style="background:radial-gradient(ellipse 50px 30px at 150px 280px,#e2c430,rgba(226,196,48,0) 75%),radial-gradient(ellipse 60px 140px at 80px 170px,#222,rgba(34,34,34,0) 75%),linear-gradient(180deg,#e1cf9a 0%,#bfa872 45%,#6a6150 75%,#3b3b3b 100%)"></div></div>
    <div class="gallery-item" style="left:868px;top:2398px;width:249px;height:271px"><div class="photo" role="img" aria-label="Hands removing a lock cylinder" style="background:radial-gradient(ellipse 80px 70px at 110px 120px,#d7a98c,rgba(215,169,140,0) 70%),linear-gradient(135deg,#c3bcb2,#6a6056)"></div></div>
    <div class="gallery-item" style="left:79px;top:2692px;width:248px;height:269px"><div class="photo" role="img" aria-label="Hand turning a door handle" style="background:radial-gradient(ellipse 90px 70px at 130px 90px,#d7aa92,rgba(215,170,146,0) 70%),linear-gradient(135deg,#d9d4cd,#8e8a86)"></div></div>
    <div class="gallery-item" style="left:341px;top:2692px;width:242px;height:269px"><div class="photo" role="img" aria-label="Hand holding a car key" style="background:radial-gradient(ellipse 60px 50px at 90px 120px,#2a2a2a,rgba(42,42,42,0) 70%),radial-gradient(ellipse 90px 80px at 150px 170px,#d9a98e,rgba(217,169,142,0) 70%),linear-gradient(135deg,#e4e4e4,#9c9c9c)"></div></div>
    <div class="gallery-item" style="left:603px;top:2770px;width:245px;height:191px"><div class="photo" role="img" aria-label="Car key at a car door handle" style="background:radial-gradient(ellipse 70px 50px at 150px 60px,#cfa088,rgba(207,160,136,0) 70%),linear-gradient(180deg,#e3e5e7 0%,#a9adb1 55%,#6f7378 100%)"></div></div>
    <div class="gallery-item" style="left:868px;top:2687px;width:249px;height:274px"><div class="photo" role="img" aria-label="Locksmith fitting a lock to a wooden door" style="background:radial-gradient(ellipse 70px 90px at 160px 150px,#3c4a78,rgba(60,74,120,0) 75%),linear-gradient(90deg,#e7d2a8 0%,#d39a55 35%,#a86c38 70%,#6b4a35 100%)"></div></div>
  </section>

  <footer class="site-footer">
    <div class="footer-head" style="left:81px">Quick Links</div>
    <ul class="quick-links"><li>Home</li><li>About Us</li><li>Services</li><li>Gallery</li><li>Contact</li></ul>
    <div class="footer-head" style="left:253px;width:205px">Contact Details</div>
    <ul class="contact-list">
      <li><svg width="14" height="18" viewBox="0 0 14 18"><path d="M7 1a6 6 0 00-6 6c0 4 6 10 6 10s6-6 6-10a6 6 0 00-6-6z" fill="#3d73b9"/><circle cx="7" cy="7" r="2" fill="#1d2331"/></svg><span><strong>Calloway Lane Locksmith</strong><br>123 Pg Duis Aute Irur Dolore<br>Srephenderit Amit In Voluptate</span></li>
      <li><svg width="14" height="14" viewBox="0 0 14 14"><path d="M2 1l3 3-1.5 1.5c1 2 3 4 5 5L10 9l3 3-2 2C6 14 0 8 0 3z" fill="#3d73b9"/></svg><strong>+ (123) 456 7890</strong></li>
      <li><svg width="14" height="14" viewBox="0 0 14 14"><rect x="1" y="2" width="12" height="10" rx="1" fill="#3d73b9"/></svg><strong>+ (123) 456 7890</strong></li>
      <li><svg width="14" height="12" viewBox="0 0 14 12"><rect x="0" y="1" width="14" height="10" fill="#3d73b9"/><path d="M0 1l7 6 7-6" fill="none" stroke="#1d2331" stroke-width="1.2"/></svg>info@callowaylanelocksmith.com</li>
    </ul>
    <div class="footer-head" style="left:532px;width:150px">Location Map</div>
    <div class="abs" role="img" aria-label="Street map of the city showing the shop location" style="left:532px;top:85px;width:233px;height:139px;border:3px solid #fff;background:radial-gradient(ellipse 70px 50px at 180px 95px,#a9c8e6,rgba(169,200,230,0) 75%),radial-gradient(ellipse 60px 40px at 40px 30px,#c9dfb8,rgba(201,223,184,0) 75%),radial-gradient(ellipse 40px 30px at 110px 60px,#f0c9a0,rgba(240,201,160,0) 75%),linear-gradient(135deg,#efeae0,#dcd6c8)"></div>
  </footer>

  <div class="footer-brand">
    <div class="footer-brand-name">Calloway Lane<br>Locksmith</div>
    <div class="follow">Follow Us:</div>
    <div class="socials"><span></span><span></span><span></span><span></span></div>
  </div>

  <div class="copyright">Copyright © 2017 Calloway Lane Locksmith. All Rights Reserved</div>
</div>
</body>
</html>
```